Information flyer for 5 day treatment flyer

I am wanting a double sided flyer for my next 5 day treatment program for addictions. I have included the copy for the flyer as an attachment.
I have also included a drop box link to my brand guidelines and my logos. The logo I prefer is the grey horse with the words Willowmere Collective under.
https://www.filecrate.example/sh/k2jtq7wn3xb5lp1/BBQr9TzLm4Kd7c8NpWvY2hsXe?dl=0

https://www.filecrate.example/s/qm8vz2kt6bw9rc4/WILLOWMERE%20COLLECTIVE%20%7C%20Brand%20Identity%20Guidelines.pdf?dl=0
I have also included a copy of an existing flyer which I like very much and a documant with the copy.
https://www.filecrate.example/sh/t7wbn3kx9zq1mv5/CCRt2pLw8-nZ4Kj7FyTuGHs_b?dl=0

I prefer simple, elegant designs please. The design needs to show my clients that I know what I am doing and I am trust worthy and a skilled professional.

Here is the drop box link to the images I have selected for this program. The tones in the images I have selected are orange/red. Please feel free to pick what you think works well.
https://www.filecrate.example/sh/mrq5jv82lnc0tfw/DDDhW392Bx6Lp88_Q7KcZnRye?dl=0

Many thanks
Marisol

```html
<!DOCTYPE html>
<html lang="en">
<head>
<meta charset="utf-8">
<title>Willowmere Collective – 5 Day Intensive Program</title>
<link href="https://fonts.googleapis.com/css2?family=Noto+Sans:wght@400;700&display=swap" rel="stylesheet">
<style>
  :root {
    --orange-deep: #ec8507;
    --orange-soft: #f5b264;
    --accent: #f15a22;
    --ink: #1b1b1b;
    --heading-ink: #2b1406;
    --brown: #3f2a1b;
    --logo-bg: #2a1a12;
    --logo-ring: #c8d2d5;
    --white: #ffffff;
  }
  * { margin: 0; padding: 0; box-sizing: border-box; }
  html, body { width: 848px; height: 1200px; overflow: hidden; background: var(--white); }
  body { font-family: "Noto Sans", "DejaVu Sans", sans-serif; color: var(--ink); }
  .flyer { position: relative; width: 848px; height: 1200px; overflow: hidden; }

  .hero-art { position: absolute; left: 0; top: 0; width: 848px; height: 740px; }

  .program-title {
    position: absolute; left: 89px; top: 46px;
    font-size: 20px; font-weight: 700; letter-spacing: 0.4px; color: var(--heading-ink);
  }
  .outcome-line {
    position: absolute; left: 113px; font-size: 14.4px; line-height: 18px; color: var(--ink);
    white-space: nowrap; transform: translateY(-9px);
  }
  .outcome-dot {
    position: absolute; left: 88px; width: 12px; height: 12px; border-radius: 50%;
    background: #444; border: 2.5px solid #c7ced2; transform: translateY(-6px);
  }

  .brand-badge {
    position: absolute; left: 52px; top: 448px; width: 144px; height: 144px; border-radius: 50%;
    background: var(--logo-bg); border: 3px solid var(--logo-ring);
    display: flex; align-items: flex-end; justify-content: center; padding-bottom: 34px;
  }
  .brand-name {
    color: var(--white); font-size: 10px; font-weight: 400; letter-spacing: 2px;
    text-align: center; line-height: 15px;
  }

  .section-title {
    position: absolute; font-size: 13.5px; font-weight: 700; color: var(--accent); letter-spacing: 0.3px;
  }
  .detail-list { position: absolute; list-style: none; font-size: 11.4px; line-height: 18.4px; }
  .detail-list li { position: relative; padding-left: 18px; }
  .detail-list li::before {
    content: ""; position: absolute; left: 0; top: 5px; width: 9px; height: 9px; border-radius: 50%; background: #111;
  }
  .investment { position: absolute; left: 78px; top: 896px; font-size: 16px; color: var(--accent); }
  .investment strong { font-size: 13.5px; letter-spacing: 0.3px; }

  .when-label { position: absolute; left: 462px; top: 756px; font-size: 14px; }
  .schedule { position: absolute; left: 461px; top: 780px; font-size: 11.4px; line-height: 18.4px; }
  .enrol-text {
    position: absolute; left: 462px; width: 320px; font-size: 11.4px; line-height: 18.4px; text-align: justify;
  }

  .footer {
    position: absolute; left: 0; top: 1114px; width: 848px; height: 86px; background: var(--brown); color: var(--white);
    font-size: 11.4px; line-height: 18.4px;
  }
  .footer-company { position: absolute; left: 40px; top: 17px; }
  .footer-company strong { letter-spacing: 0.5px; }
  .footer-contact { position: absolute; right: 48px; top: 20px; text-align: right; }
</style>
</head>
<body>
<main class="flyer">
  <svg class="hero-art" viewBox="0 0 848 740" preserveAspectRatio="none">
    <defs>
      <linearGradient id="sunsetWash" x1="0" y1="0" x2="0" y2="1">
        <stop offset="0" stop-color="#ec8507"/>
        <stop offset="0.35" stop-color="#f08f1a"/>
        <stop offset="0.62" stop-color="#f6bd7c"/>
        <stop offset="0.82" stop-color="#fde9d3"/>
        <stop offset="1" stop-color="#ffffff"/>
      </linearGradient>
      <linearGradient id="sandTones" x1="0" y1="1" x2="1" y2="0">
        <stop offset="0" stop-color="#3e2640"/>
        <stop offset="0.45" stop-color="#6c4a5a"/>
        <stop offset="0.8" stop-color="#a57b5c"/>
        <stop offset="1" stop-color="#d4a66e"/>
      </linearGradient>
    </defs>
    <rect x="0" y="0" width="848" height="740" fill="url(#sunsetWash)"/>
    <path role="img" aria-label="Photograph: a heart drawn in sand at golden hour"
      d="M0 664 C 260 560, 620 520, 848 246 L848 664 C 720 668, 600 700, 470 700 C 330 700, 180 690, 90 700 C 50 705, 20 715, 0 732 Z"
      fill="url(#sandTones)"/>
  </svg>

  <h1 class="program-title">DURING THIS 12 DAY INTENSIVE PROGRAM YOU WILL:</h1>

  <span class="outcome-dot" style="top:101px"></span>
  <span class="outcome-dot" style="top:121px"></span>
  <span class="outcome-dot" style="top:142px"></span>
  <span class="outcome-dot" style="top:163px"></span>
  <span class="outcome-dot" style="top:185px"></span>
  <span class="outcome-dot" style="top:225px"></span>
  <span class="outcome-dot" style="top:246px"></span>
  <span class="outcome-dot" style="top:286px"></span>
  <span class="outcome-dot" style="top:308px"></span>
  <span class="outcome-dot" style="top:329px"></span>
  <span class="outcome-dot" style="top:351px"></span>
  <span class="outcome-dot" style="top:390px"></span>

  <p class="outcome-line" style="top:100px">Identify what you need to do for yourself to stop destructive relationship</p>
  <p class="outcome-line" style="top:119px">patterns.</p>
  <p class="outcome-line" style="top:140px">Learn how to protect yourself from feeling overwhelmed or drained in close</p>
  <p class="outcome-line" style="top:159px">relationships.</p>
  <p class="outcome-line" style="top:180px">Release emotional baggage from past adult relationships.</p>
  <p class="outcome-line" style="top:201px">Significantly heal childhood abandonment and engulfment issues.</p>
  <p class="outcome-line" style="top:223px">Identify the subconscious negative beliefs that are sabotaging you from</p>
  <p class="outcome-line" style="top:242px">having the relationship you desire.</p>
  <p class="outcome-line" style="top:263px">Release childhood trauma out of your body from abuse and neglect</p>
  <p class="outcome-line" style="top:284px">Learn how to set healthy boundaries - physically, emotionally, spiritually,</p>
  <p class="outcome-line" style="top:303px">intellectually and sexually.</p>
  <p class="outcome-line" style="top:324px">Differentiate between needs and values - the drivers in relationships.</p>
  <p class="outcome-line" style="top:346px">Identify your needs and values and determine steps to take to meet them.</p>
  <p class="outcome-line" style="top:367px">Free yourself of shame, guilt and fear from childhood and adult relationships.</p>
  <p class="outcome-line" style="top:389px">Communicate your needs and ask for what you want without feeling too</p>
  <p class="outcome-line" style="top:407px">embarrassed or vulnerable.</p>

  <div class="brand-badge">
    <p class="brand-name">WILLOWMERE<br>COLLECTIVE</p>
  </div>

  <h2 class="section-title" style="left:78px;top:740px">INCLUSIONS</h2>
  <ul class="detail-list" style="left:78px;top:763px">
    <li>A pre-assessment phone consult</li>
    <li>Relevant on online diagnostic survey‘s</li>
    <li>Integrated Equine Assisted Psychotherapy</li>
    <li>Ropes course</li>
    <li>All course materials (notebook, writing materials),<br>Morning and afternoon tea daily,</li>
  </ul>

  <p class="investment"><strong>INVESTMENTS :</strong>&nbsp; $2250 including GST</p>

  <h2 class="section-title" style="left:78px;top:934px">TERMS &amp; CONDITIONS</h2>
  <ul class="detail-list" style="left:78px;top:959px">
    <li>A non-refundable deposit of $500 is required to<br>hold your place.</li>
    <li>Enrolments with full payment is required by<br>Tuesday, 23th October 2018.</li>
    <li>Orbitcard transactions incur a 3.3% merchant fee, Veyra<br>and Meridian Card 2.5%.</li>
    <li>Tap-and-pay facility available.</li>
  </ul>

  <h2 class="section-title" style="left:462px;top:729px">PROGRAM DETAILS</h2>
  <p class="when-label">WHEN</p>
  <p class="schedule">
    Thursday 25th October 6:00pm – 9:00pm<br>
    Friday, 26th October 9:00pm – 5:00pm<br>
    Saturday, 27th October 9:00pm – 9:00pm<br>
    Sunday, 28th October 9:00pm – 5:00pm<br>
    Monday, 29th October 9:00pm – 4:00pm
  </p>

  <h2 class="section-title" style="left:463px;top:901px">ENROLMENT PROCESS</h2>
  <p class="enrol-text" style="top:927px">This 5 day program is limited in numbers and offers individual and group time. Enrolments close Friday, 19th October 2018.</p>
  <p class="enrol-text" style="top:992px">To book your place, register your interest or find out more about this program please call<br>Marisol 0400 317 264</p>
  <p class="enrol-text" style="top:1054px">Out of town participants please contact our office for assistance with accommodation if required.</p>

  <footer class="footer">
    <p class="footer-company"><strong>The Willowmere Collective Pty Ltd.</strong><br>ABN 41 302 778 619<br>27 Fernbrook Road, Kurrajong NSW 2758</p>
    <p class="footer-contact">Phone: 0400 317 264<br>Email: marisol@willowmerecollective.example</p>
  </footer>
</main>
</body>
</html>
```